Poster Design

Hello,

My name is Rowan Pickett and I run a vidora channel called 'CrumbleDiary'. I want a poster made for those who watch my video to purchase and put on their wall at home. The poster will be all text and as you can see, I've attached a few examples of posters which I would like it to be similar to. I use a lot of the colour #ab6f7f so it would be good to incorporate this in somewhere (maybe the background colour).
I would like the poster to say:
"Do More Of What Makes YOU Happy"
I need this poster to be for sale ready for christmas, so Im going to need the designs created as soon as possible. Im sorry for the rush.
Have fun with it and feel free to upload multiple versions of a design as well as a few designs if you like.
I look forward to seeing what you come up with.
Rowan
(Of course I will need to own all rights once the payment has been made)

```html
<!DOCTYPE html>
<html lang="en">
<head>
<meta charset="utf-8">
<title>Do More Of What Makes You Happy — Poster</title>
<link rel="stylesheet" href="https://fonts.googleapis.com/css2?family=Montserrat:wght@900&family=Josefin+Sans:wght@200&display=swap">
<style>
  :root {
    --paper: #fdf3f2;
    --wash-light: #f9d3d4;
    --wash-mid: #f3aab0;
    --wash-deep: #ee8f99;
    --ink-bold: #e5325c;
    --ink-thin: #e6627c;
  }
  html, body {
    margin: 0;
    padding: 0;
    overflow: hidden;
    background: var(--paper);
  }
  .poster {
    position: relative;
    width: 848px;
    height: 1200px;
    background: var(--paper);
    overflow: hidden;
  }
  .poster__wash {
    position: absolute;
    left: 22px;
    top: 22px;
    width: 804px;
    height: 1156px;
  }
  .poster__type {
    position: absolute;
    inset: 0;
    width: 848px;
    height: 1200px;
  }
  .headline-bold {
    font-family: "Montserrat", Arial, sans-serif;
    font-weight: 900;
    fill: var(--ink-bold);
    fill-opacity: 0.72;
  }
  .headline-thin {
    font-family: "Josefin Sans", Helvetica, sans-serif;
    font-weight: 200;
    fill: var(--ink-thin);
    fill-opacity: 0.55;
  }
</style>
</head>
<body>
<main class="poster">
  <svg class="poster__wash" viewBox="0 0 804 1156" role="img" aria-label="Soft pink watercolour wash background with pale blotches">
    <defs>
      <linearGradient id="wash-base" x1="0" y1="0" x2="0.3" y2="1">
        <stop offset="0" stop-color="var(--wash-mid)"/>
        <stop offset="0.5" stop-color="var(--wash-light)"/>
        <stop offset="1" stop-color="var(--wash-mid)"/>
      </linearGradient>
      <radialGradient id="wash-glow" cx="0.5" cy="0.45" r="0.5">
        <stop offset="0" stop-color="#ffffff" stop-opacity="0.45"/>
        <stop offset="1" stop-color="#ffffff" stop-opacity="0"/>
      </radialGradient>
      <radialGradient id="wash-shade" cx="0.15" cy="0.75" r="0.45">
        <stop offset="0" stop-color="var(--wash-deep)" stop-opacity="0.6"/>
        <stop offset="1" stop-color="var(--wash-deep)" stop-opacity="0"/>
      </radialGradient>
    </defs>
    <rect width="804" height="1156" fill="url(#wash-base)"/>
    <rect width="804" height="1156" fill="url(#wash-shade)"/>
    <rect width="804" height="1156" fill="url(#wash-glow)"/>
  </svg>

  <svg class="poster__type" viewBox="0 0 848 1200">
    <title>Do More Of What Makes You Happy</title>
    <text class="headline-bold" x="42" y="366" font-size="197" textLength="770" lengthAdjust="spacingAndGlyphs">DO MORE</text>
    <text class="headline-thin" x="40" y="557" font-size="147" textLength="772" lengthAdjust="spacingAndGlyphs">OF WHAT</text>
    <text class="headline-thin" x="42" y="721" font-size="125" textLength="770" lengthAdjust="spacingAndGlyphs">MAKES YOU</text>
    <text class="headline-bold" x="48" y="1012" font-size="264" textLength="749" lengthAdjust="spacingAndGlyphs">HAPPY</text>
  </svg>
</main>
</body>
</html>
```